vermalo web design

- Company / Site Description
We are developing a website that will allow anyone in Europe to find in one click, cultural things to do (Exhibition, Museum, Monument, Zoo, Aquarium, Archaeological site…) with friends or family, and to organize the visit (book a ticket / a private visit, book a restaurant nearby…).

Examples
1. You're in London with your girlfriend, it's saturday 10 am, you have two hours to spend and you want to see an exhibition. We provide you in one click all the exhibition matching your location / time and date.

2. You're in Berlin with some friends, it's thursday night you want to go out, but you don't know what to do. We provide you a list of experience, you can select for instance "I want to be on top of the world", and we show you a list of venues matching the selected experience / date / time /location of your request.

- Brand name : Vermalo
- Activity : Cultural Leisure, cultural entertainment

- Target audience
Broad target will be between 20 and 55. Core target will be between 25 and 40. Most likely to live in a city and in Europe.

- Behaviours and preferences
Our user is under time constraint (few minutes to find and choose his visit), idea constraint (is not sure about what to do and see) and money constraint.
He wants to have an easy to use website, not cluttered with information, focussed on added value information. He wants to have a website which is modern, fun and elegant that he will deem as professional and trustworthy.

- Our expectations (Do’s and Don’t)
We want to move away from traditional design. We want some OUT OF THE BOX design. Think of a website design that will look like an app design.
We want to make an awesome / extra ordinary /remember-able design. The design must be so cool, that the user wants to come back to the site. In two words: THINK EXTRAORDINARY.
You can use photos to help the user understand functions. If you use photo, use creative commons license photo.
Avoid black colors

- Functional Requirements
We need Four pages:
1. Home Page (desktop and mobile version): it’s both the homepage and the assistant page. This page will allow the user to find in one click his visit (please refer to the pdf file Assistant home page). The page must be self-explanatory for a first time user.
2. Assistant result page (desktop version): it’s the page that display the results found by the assistant based on the criteria search (please refer to the pdf file mockup - Assistant result page)
3. Site / Event page (desktop version): it’s the page that display each result information (please refer to the pdf file mockup – Event / Site Page)
The pdf files list all the elements include in each page + gives you a mockup of each page (just to put in perspective the element required). You are completely free about the design.
We don’t have the logo yet. Use a dummy logo for your page design.
The selected winner can expect to work with us immediately after the contest and on a on a regular basis later on.

- Technical Requirements
No Flash
For the winner, we will manage the CSS you will just need to provide :
. One PSD file containing all the pages
. Inside the PSD file we want for each page two groups: the first group will embed the desktop design, the second group will embed the responsive mobile design (Home Page only).
In total there should be 4 groups inside the PSD file (3 desktop groups, 1 mobile group).
Each group must contain all the elements specified in the pdf file

Website we like
http://demo.plandorix.example/?theme=Velunt
http://rosabel.quintorhub.example/#home
http://blogsite.fenk.daltoroute.example/2/
http://demo.plandorix.example/?theme=Mosaru
http://www.quarnivo.example/themes/lumbe/
http://gridmarket.example/item/tav-responsive-photography-blog-theme/full_screen_preview/8146027
http://items.zkvortel.example/?product=example
http://uk.harnoway.example

Reason: Due to the request of several designers, we have agreed to add 7 additional days to the contest deadline. Thank you. The vermalo team

Reason: We still need to collect all the votes. Sorry for the delay.

Reason: Hello, We extend the contest deadline, in order to collect all the votes from the poll. We should have everything finalized by sunday. Thank you vermalo team

```html
<!DOCTYPE html>
<html lang="fr">
<head>
<meta charset="utf-8">
<title>Vermalo – Musée de Valmorin</title>
<link href="https://fonts.googleapis.com/css2?family=Arimo:ital,wght@0,400;0,700;1,400&display=swap" rel="stylesheet">
<style>
:root{
  --brand:#2a8fc1;
  --brand-dark:#2468b4;
  --text:#4a4a4a;
  --muted:#9a9a9a;
  --line:#d9d9d9;
  --panel:#f1f1f1;
  --btn:#e6e8ea;
  --icon:#666a6e;
  --footer:#4f4f4f;
  --white:#ffffff;
}
*{box-sizing:border-box;margin:0;padding:0}
html,body{width:1200px;height:693px;overflow:hidden;background:var(--white);font-family:"Arimo",Arial,sans-serif;color:var(--text)}
.page{position:relative;width:1200px;height:693px}
.abs{position:absolute}

/* header */
.site-header{left:0;top:0;width:1200px;height:97px;border-bottom:1px solid var(--line)}
.brand{left:173px;top:30px;font-size:34px;font-weight:700;color:var(--brand);letter-spacing:-1.5px}
.nav-tab{top:0;height:96px;display:flex;align-items:center;justify-content:center;font-size:14px;color:#555;border-left:1px solid var(--line)}
.nav-tab.active{color:var(--brand)}
.nav-tab.active::after{content:"";position:absolute;left:0;right:0;bottom:0;height:4px;background:#6cb3d3}
.tab-assistant{left:375px;width:142px}
.tab-favourites{left:517px;width:151px;border-right:1px solid var(--line)}
.search{left:728px;top:38px;width:181px;height:29px;border:1px solid var(--line)}
.search svg{position:absolute;right:9px;top:7px}
.avatar{left:946px;top:19px;width:63px;height:58px;background:linear-gradient(135deg,#d8d8d8,#8a8a8a);border:1px solid var(--line)}
.avatar-toggle{left:1009px;top:19px;width:21px;height:58px;border:1px solid var(--line);border-left:none;background:#f4f4f4}
.avatar-toggle svg{position:absolute;left:5px;top:25px}

/* media */
.photo-frame{left:172px;top:143px;width:418px;height:253px;border:1px solid var(--line);padding:4px;background:var(--white)}
.photo{width:100%;height:100%;background:radial-gradient(ellipse at 40% 60%,#b88a3a 0%,#6b4a1c 35%,#2a1c10 70%,#151010 100%)}
.play{left:350px;top:225px;width:62px;height:62px;border-radius:50%;background:rgba(255,255,255,.22)}
.action{left:607px;width:52px;height:47px;background:var(--btn);border:1px solid #c9cbcd;display:flex;align-items:center;justify-content:center}

/* share */
.share-bar{left:691px;top:145px;width:338px;height:47px;border:1px solid var(--line);background:linear-gradient(#f7f7f7,#ececec)}
.share-label{left:22px;top:16px;font-size:12px;font-style:italic;color:#666}
.count{top:12px;height:23px;display:flex;border:1px solid #cfcfcf;background:var(--white);font-size:11px;color:#666}
.count .sq{width:23px;height:21px}
.count .num{width:26px;display:flex;align-items:center;justify-content:center}
.share-panel{left:691px;top:198px;width:338px;height:220px;border:1px solid var(--line);background:var(--panel)}
.close{left:1005px;top:204px;width:19px;height:19px;border-radius:50%;background:var(--brand-dark);color:var(--white);font-size:11px;display:flex;align-items:center;justify-content:center;border:1px solid #fff}
.field{left:712px;width:300px;border:1px solid #c3c3c3;background:var(--white);font-size:10.5px;color:var(--muted);padding:12px 15px}
.comment{top:225px;height:57px}
.preview{top:291px;height:77px;line-height:17px;padding-top:10px}
.preview a{display:block;margin-top:6px;color:var(--brand-dark);font-style:italic;text-decoration:none}
.share-btn{left:930px;top:379px;width:82px;height:24px;background:linear-gradient(#3f8fd6,var(--brand-dark));color:var(--white);font-size:12px;display:flex;align-items:center;justify-content:center;border-radius:2px}

/* details */
.title{left:173px;top:436px;font-size:21px;color:var(--brand)}
.rating{left:362px;top:437px;display:flex;align-items:center;gap:5px;font-size:11px;color:#555}
.subtitle{left:173px;top:469px;font-size:14.5px;color:#555}
.description{left:173px;top:503px;width:850px;font-size:10.5px;line-height:21.5px;color:#555}

/* footer */
.site-footer{left:0;top:624px;width:1200px;height:69px;background:var(--footer)}
.language{left:172px;top:30px;font-size:10px;color:var(--white)}
.language b{color:#39a6dc}
.to-top{left:992px;top:17px;width:34px;height:34px;border:1px solid #777;border-radius:50%}
.to-top svg{position:absolute;left:10px;top:11px}
.version{left:1103px;top:28px;font-size:11.5px;color:#bbb}
</style>
</head>
<body>
<div class="page">

  <header class="site-header abs">
    <div class="brand abs">Vermalo</div>
    <nav>
      <div class="nav-tab tab-assistant active abs">My Assistant</div>
      <div class="nav-tab tab-favourites abs">My Favourites</div>
    </nav>
    <div class="search abs">
      <svg width="14" height="14" viewBox="0 0 14 14"><circle cx="5.5" cy="5.5" r="4.3" fill="none" stroke="#ccc" stroke-width="1.6"/><line x1="8.7" y1="8.7" x2="13" y2="13" stroke="#ccc" stroke-width="2"/></svg>
    </div>
    <div class="avatar abs" role="img" aria-label="User profile photo"></div>
    <div class="avatar-toggle abs">
      <svg width="10" height="6" viewBox="0 0 10 6"><path d="M1 1l4 4 4-4" fill="none" stroke="#777" stroke-width="1.6"/></svg>
    </div>
  </header>

  <div class="photo-frame abs">
    <div class="photo" role="img" aria-label="Night view of the museum courtyard with a lit glass pyramid and palace facade"></div>
  </div>
  <div class="play abs"></div>

  <div class="action abs" style="top:144px">
    <svg width="22" height="26" viewBox="0 0 22 26"><path d="M3 25C3 14 8 9 15 9V4l6 8-6 8v-5c-5 0-9 3-12 10z" fill="var(--icon)"/></svg>
  </div>
  <div class="action abs" style="top:196px">
    <svg width="26" height="22" viewBox="0 0 26 22"><path d="M13 21L2.5 10.5A6 6 0 0 1 13 3a6 6 0 0 1 10.5 7.5z" fill="var(--icon)"/></svg>
  </div>
  <div class="action abs" style="top:247px">
    <svg width="24" height="23" viewBox="0 0 24 23"><path d="M12 1l3.4 7 7.6 1-5.5 5.3 1.3 7.7L12 18.3 5.2 22l1.3-7.7L1 9l7.6-1z" fill="var(--icon)"/></svg>
  </div>
  <div class="action abs" style="top:299px">
    <svg width="28" height="22" viewBox="0 0 28 22"><ellipse cx="14" cy="9" rx="13" ry="8" fill="var(--icon)"/><path d="M6 15l-3 6 8-4z" fill="var(--icon)"/><text x="14" y="13" font-size="10" fill="#fff" text-anchor="middle" font-family="Arimo,sans-serif">5</text></svg>
  </div>

  <div class="share-bar abs">
    <span class="share-label abs">Share</span>
    <div class="count abs" style="left:70px"><span class="sq" style="background:#d94a38"></span><span class="num">6</span></div>
    <div class="count abs" style="left:148px"><span class="sq" style="background:#3b5a98"></span><span class="num">15</span></div>
    <div class="count abs" style="left:225px"><span class="sq" style="background:#7cc1de"></span><span class="num">4</span></div>
  </div>

  <div class="share-panel abs"></div>
  <div class="close abs">x</div>
  <div class="field comment abs">Add a Comment</div>
  <div class="field preview abs">
    Une visite au Musée de Valmorin, un moment à ne pas rater<br>
    de Valmorin, un moment à ne pas rater
    <a href="#">www.vermalo.com</a>
  </div>
  <div class="share-btn abs">SHARE</div>

  <h1 class="title abs" style="font-weight:400">Musée de Valmorin</h1>
  <div class="rating abs">
    <svg width="24" height="23" viewBox="0 0 24 23"><path d="M12 1l3.4 7 7.6 1-5.5 5.3 1.3 7.7L12 18.3 5.2 22l1.3-7.7L1 9l7.6-1z" fill="#f2b233" stroke="#d8931c"/><text x="12" y="16" font-size="9" text-anchor="middle" fill="#5a3a00" font-family="Arimo,sans-serif">9</text></svg>
    <span>154 votes</span>
  </div>
  <div class="subtitle abs">Paris │Arts décoratifs -Beaux-Arts -Histoire</div>
  <p class="description abs">Le musée de Valmorin, ancienne demeure des rois de France, est depuis deux siècles l'un des plus grands musées du monde. Ses collections sont réparties en huit départements : Antiquités orientales, égyptiennes, grecques, étrusques et romaines, Peintures, Sculptures, Objets d'art, Arts de l'Islam et Arts graphiques du Moyen Âge jusqu'à 1848.Le musée de Valmorin, ancienne demeure des rois de France, est depuis deux siècles l'un des plus grands musées du monde. Ses collections sont réparties en huit départements : Antiquités orientales, égyptiennes, grecques, étrusques et romaines, Peintures, Sculptures, Objets d'art, Arts de l'Islam et Arts graphiques du Moyen Âge jusqu'à 1848.</p>

  <footer class="site-footer abs">
    <div class="language abs">LANGUAGE : <b>ENGLISH</b></div>
    <div class="to-top abs">
      <svg width="12" height="8" viewBox="0 0 12 8"><path d="M1 7l5-5 5 5" fill="none" stroke="#888" stroke-width="2"/></svg>
    </div>
    <div class="version abs">C8</div>
  </footer>

</div>
</body>
</html>
```